HSPT Foldable Flyer

Design a flyer, foldable. To fit in an envelope and/or drop off at doctor office for an outpatient physical therapy clinic, Harborstrengthpt.com.
Emphasis on appointments two weeks out, taking new patients, and use website for photos

```html
<!DOCTYPE html>
<html lang="en">
<head>
<meta charset="utf-8">
<title>Harbor Strength Physical Therapy – Flyer</title>
<link rel="stylesheet" href="https://fonts.googleapis.com/css2?family=Chakra+Petch:wght@600;700&family=Nunito+Sans:wght@400&family=Montserrat:wght@500&display=swap">
<style>
  :root {
    --navy: #2f527d;
    --navy-text: #2d4f7a;
    --ink: #1d1d1f;
    --white: #ffffff;
    --ring-faint: #7f9cc0;
    --photo-a: #aebccb;
    --photo-b: #3c4f66;
  }
  * { margin: 0; padding: 0; box-sizing: border-box; }
  html, body { width: 927px; height: 1200px; overflow: hidden; background: var(--white); }
  .flyer { position: relative; width: 927px; height: 1200px; overflow: hidden; background: var(--white); font-family: "Nunito Sans", sans-serif; color: var(--ink); }

  .brand { position: absolute; left: 47px; top: 30px; color: var(--navy-text); font-family: "Chakra Petch", sans-serif; font-weight: 700; }
  .brand-name { font-size: 48px; line-height: 1; letter-spacing: -0.5px; }
  .brand-sub { font-size: 15px; letter-spacing: 2px; margin-top: 6px; text-align: right; }

  .hero-band { position: absolute; left: 0; top: 130px; width: 520px; height: 456px; background: var(--navy); }
  .hero-circle { position: absolute; left: 386px; top: 5px; width: 704px; height: 704px; }
  .ring-text { font-family: "Montserrat", sans-serif; font-weight: 500; font-size: 16px; letter-spacing: 3px; }

  .headline { position: absolute; left: 47px; top: 205px; font-family: "Chakra Petch", sans-serif; font-weight: 700; font-size: 51px; line-height: 58px; color: var(--white); letter-spacing: 1px; }
  .cta { position: absolute; left: 46px; top: 452px; width: 305px; height: 51px; background: var(--white); color: var(--navy-text); font-family: "Chakra Petch", sans-serif; font-weight: 700; font-size: 19px; letter-spacing: 0.6px; display: flex; align-items: center; justify-content: center; }

  .section-title { position: absolute; font-family: "Chakra Petch", sans-serif; font-weight: 700; color: var(--navy-text); }
  .rule { position: absolute; height: 3px; width: 101px; background: var(--navy); }
  .body-copy { position: absolute; font-size: 13px; line-height: 22px; color: var(--ink); }

  .philosophy-title { left: 46px; top: 636px; font-size: 26px; }
  .philosophy-rule { left: 46px; top: 675px; }
  .philosophy-copy { left: 47px; top: 700px; width: 390px; }

  .patients-title { left: 46px; top: 838px; font-size: 25px; line-height: 36px; letter-spacing: 0.4px; }
  .patients-rule { left: 47px; top: 1000px; }
  .patients-copy { left: 47px; top: 1018px; width: 390px; }

  .services-title { left: 506px; top: 747px; font-size: 26px; }
  .services-rule { left: 509px; top: 790px; }

  .service { position: absolute; left: 506px; width: 360px; height: 66px; }
  .service-icon { position: absolute; left: 0; top: 0; width: 65px; height: 65px; }
  .service-name { position: absolute; left: 75px; top: -7px; font-family: "Chakra Petch", sans-serif; font-weight: 700; font-size: 15px; color: var(--ink); letter-spacing: 0.4px; }
  .service-desc { position: absolute; left: 76px; top: 17px; width: 270px; font-size: 14px; line-height: 22px; color: var(--ink); }

  .contact-bar { position: absolute; left: 47px; top: 1142px; width: 834px; height: 46px; border-radius: 23px; background: var(--navy); color: var(--white); font-family: "Chakra Petch", sans-serif; font-weight: 700; font-size: 15px; letter-spacing: 0.4px; }
  .contact-phone { position: absolute; left: 42px; top: 0; height: 46px; display: flex; align-items: center; gap: 10px; }
  .contact-mail { position: absolute; left: 505px; top: 0; height: 46px; display: flex; align-items: center; gap: 12px; }
  .seal { position: absolute; left: 426px; top: 1123px; width: 75px; height: 75px; border-radius: 50%; background: var(--white); border: 2px solid var(--navy); }
</style>
</head>
<body>
<div class="flyer">

  <div class="brand">
    <div class="brand-name">Harbor Strength</div>
    <div class="brand-sub">PHYSICAL THERAPY</div>
  </div>

  <div class="hero-band"></div>

  <svg class="hero-circle" viewBox="0 0 704 704" aria-hidden="false">
    <defs>
      <radialGradient id="photoTone" cx="40%" cy="40%" r="70%">
        <stop offset="0" stop-color="var(--photo-a)"/>
        <stop offset="1" stop-color="var(--photo-b)"/>
      </radialGradient>
      <path id="ringPath" d="M352,30 A322,322 0 1 1 351.9,30"/>
    </defs>
    <circle cx="352" cy="352" r="352" fill="var(--navy)"/>
    <circle cx="352" cy="352" r="291" fill="url(#photoTone)" role="img" aria-label="Photo of a physical therapist stretching a patient's leg on a treatment table"/>
    <text class="ring-text" fill="var(--white)"><textPath href="#ringPath" startOffset="2%">PHYSICAL THERAPY</textPath></text>
    <text class="ring-text" fill="var(--white)"><textPath href="#ringPath" startOffset="27%">PHYSICAL THERAPY</textPath></text>
    <text class="ring-text" fill="var(--ring-faint)"><textPath href="#ringPath" startOffset="52%">PHYSICAL THERAPY</textPath></text>
    <text class="ring-text" fill="var(--ring-faint)"><textPath href="#ringPath" startOffset="77%">PHYSICAL THERAPY</textPath></text>
  </svg>

  <h1 class="headline">HELPING YOU<br>MOVE BETTER<br>AND FEEL<br>BETTER</h1>
  <div class="cta">SCHEDULE AN APPOINTMENT</div>

  <h2 class="section-title philosophy-title">OUR PHILOSOPHY</h2>
  <div class="rule philosophy-rule"></div>
  <p class="body-copy philosophy-copy">At Harbor Strength Physical Therapy we strive to provide the Harbor region with exceptional care and high quality outpatient physical therapy services. We will work with you in your road to recovery to assist in reducing your pain and improving the way you feel and move.</p>

  <h2 class="section-title patients-title">NOW ACCEPTING NEW PATIENTS<br>APPOINTMENTS AVAILABLE<br>STARTING TWO WEEKS FROM<br>TODAY.</h2>
  <div class="rule patients-rule"></div>
  <p class="body-copy patients-copy">We are here to provide quality one on one care, evidence based treatment&nbsp; and to assist in providing you with the quality of life that you deserve.</p>

  <h2 class="section-title services-title">OUR SERVICES</h2>
  <div class="rule services-rule"></div>

  <div class="service" style="top:818px">
    <svg class="service-icon" viewBox="0 0 65 65">
      <circle cx="32.5" cy="32.5" r="32.5" fill="var(--navy)"/>
      <circle cx="32.5" cy="32.5" r="26" fill="none" stroke="var(--white)" stroke-width="1.5"/>
      <rect x="25" y="19" width="15" height="26" rx="6" fill="var(--white)"/>
      <path d="M32.5 28v10M27.5 33h10" stroke="var(--navy)" stroke-width="2"/>
    </svg>
    <div class="service-name">HANDS ON CARE</div>
    <div class="service-desc">Personalized and professional care to meet your needs.</div>
  </div>

  <div class="service" style="top:920px">
    <svg class="service-icon" viewBox="0 0 65 65">
      <circle cx="32.5" cy="32.5" r="32.5" fill="var(--navy)"/>
      <circle cx="32.5" cy="32.5" r="26" fill="none" stroke="var(--white)" stroke-width="1.5"/>
      <rect x="23" y="22" width="20" height="18" rx="3" fill="none" stroke="var(--white)" stroke-width="2"/>
      <path d="M29 22v-3h8v3M33 26v10M28 31h10" stroke="var(--white)" stroke-width="2" fill="none"/>
      <path d="M18 45h14l8-4" stroke="var(--white)" stroke-width="2" fill="none"/>
    </svg>
    <div class="service-name">ONE ON ONE TREATMENT</div>
    <div class="service-desc">Evidence based driven care to assist you.</div>
  </div>

  <div class="service" style="top:1021px">
    <svg class="service-icon" viewBox="0 0 65 65">
      <circle cx="32.5" cy="32.5" r="32.5" fill="var(--navy)"/>
      <circle cx="32.5" cy="32.5" r="26" fill="none" stroke="var(--white)" stroke-width="1.5"/>
      <path d="M32.5 37 l-7-7 a4 4 0 0 1 7-5 a4 4 0 0 1 7 5z" fill="var(--white)"/>
      <path d="M20 30 l6 12h4M45 30 l-6 12h-4" stroke="var(--white)" stroke-width="2.5" fill="none" stroke-linecap="round"/>
    </svg>
    <div class="service-name">HEALTH AND WELLNESS</div>
    <div class="service-desc">Goal driven treatment to maintain and improve your quality of life.</div>
  </div>

  <div class="contact-bar">
    <div class="contact-phone">
      <svg width="22" height="22" viewBox="0 0 24 24"><path d="M6.6 2.5l3 3.5-2 2.5c1.2 2.6 3.3 4.7 5.9 5.9l2.5-2 3.5 3-1.8 3.1C11 18.8 5.2 13 3.5 4.3z" fill="var(--white)"/></svg>
      <span>555-014-2870&nbsp; OR &nbsp;555-014-3961</span>
    </div>
    <div class="contact-mail">
      <svg width="25" height="18" viewBox="0 0 25 18"><rect x="1" y="1" width="23" height="16" fill="none" stroke="var(--white)" stroke-width="2"/><path d="M1 1l11.5 9L24 1M1 17l8-7M24 17l-8-7" stroke="var(--white)" stroke-width="1.6" fill="none"/></svg>
      <span>INFO@HARBORSTRENGTHPT.COM</span>
    </div>
  </div>
  <div class="seal"></div>

</div>
</body>
</html>
```